ORVANE SYSTEMS LTD

See website just wanted it updated and more fresh ; https://www.orvane-sys.co.uk

Coding

Coded - Design and coding required

Colors

Designer to choose colors to be used in the design.

```html
<!DOCTYPE html>
<html lang="en">
<head>
<meta charset="utf-8">
<title>Orvane Systems – Education, Support and Installation</title>
<link rel="stylesheet" href="https://fonts.googleapis.com/css2?family=Montserrat:wght@400;500;600;700&family=Raleway:wght@400;500&family=Arimo:wght@400;700&family=Open+Sans:ital,wght@0,400;0,600;0,700;1,400&display=swap">
<style>
:root{
  --orange:#f26a2a;
  --blue:#1a73c7;
  --blue-deep:#0f5ca8;
  --ink:#222;
  --muted:#6c6c6c;
  --pale:#e8f0f8;
  --footer:#262a30;
  --white:#fff;
}
*{box-sizing:border-box;margin:0;padding:0}
html,body{width:1200px;height:4532px;overflow:hidden}
body{position:relative;font-family:"Open Sans",sans-serif;color:var(--ink);background:var(--white)}
.abs{position:absolute}
.section-title{font-family:"Raleway",sans-serif;font-weight:400;font-size:25px;color:var(--ink);display:flex;align-items:center;gap:14px}
.section-title::after{content:"";width:24px;height:2px;background:var(--orange)}
.centered{left:0;width:1200px;justify-content:center}
.btn{position:absolute;display:flex;align-items:center;justify-content:center;font-family:"Montserrat",sans-serif;font-size:15px;font-weight:500;border-radius:4px 22px 4px 4px;text-decoration:none}
.btn-orange{background:var(--orange);color:var(--white)}
.btn-white{background:var(--white);color:var(--ink)}
.btn-outline{border:2px solid var(--orange);color:var(--orange);background:var(--white);font-family:"Arimo",sans-serif;font-weight:700;font-size:15px}
.rule{position:absolute;left:0;width:1200px;height:8px;background:var(--orange)}

/* header */
.site-header{left:0;top:0;width:1200px;height:70px;background:var(--white)}
.brand{display:flex;align-items:center;gap:8px;font-family:"Montserrat",sans-serif;font-weight:600;color:var(--blue)}
.brand-mark{width:22px;height:22px;border:2px solid var(--orange);border-radius:3px}
.nav a{position:absolute;top:24px;font-family:"Raleway",sans-serif;font-size:15px;color:#555;text-decoration:none}
.nav .active{left:468px;top:16px;width:92px;height:38px;border:2px solid var(--orange);border-radius:6px;color:var(--orange);font-weight:500;display:flex;align-items:center;justify-content:center}

/* hero */
.hero{left:0;top:70px;width:1200px;height:490px;background:linear-gradient(135deg,#0b2748 0%,#1d5a92 45%,#0e2f55 100%)}
.hero h1{left:0;width:1200px;top:154px;text-align:center;font-family:"Montserrat",sans-serif;font-weight:700;font-size:29px;line-height:31px;color:var(--white)}
.hero p{left:340px;width:520px;top:226px;text-align:center;font-family:"Montserrat",sans-serif;font-size:13px;line-height:26px;color:var(--white)}

/* about */
.photo-frame{border:3px solid var(--orange);border-radius:30px;padding:7px;background:var(--white)}
.photo{width:100%;height:100%;border-radius:24px}
.body-copy{font-size:15px;line-height:26px;color:var(--muted)}

/* support band */
.band{left:0;width:1200px;background:linear-gradient(120deg,var(--blue-deep),var(--blue))}
.band .body-copy{color:var(--white)}

/* services */
.card{position:absolute;width:296px;height:500px;border-radius:14px;background:var(--white);box-shadow:0 4px 18px rgba(0,0,0,.12);text-align:center}
.card.featured{background:var(--orange);color:var(--white)}
.card .icon{position:absolute;left:83px;top:40px;width:130px;height:130px;border-radius:50%;background:#fde3d6;display:flex;align-items:center;justify-content:center}
.card .icon span{width:110px;height:110px;border-radius:50%;background:var(--orange);display:flex;align-items:center;justify-content:center}
.card.featured .icon{background:rgba(255,255,255,.4)}
.card.featured .icon span{background:var(--white)}
.card h3{position:absolute;left:0;width:296px;top:210px;font-family:"Open Sans",sans-serif;font-weight:700;font-size:24px;line-height:33px;color:var(--ink)}
.card.featured h3{color:var(--white)}
.card .card-copy{position:absolute;left:14px;width:268px;top:288px;font-family:"Arimo",sans-serif;font-size:16px;line-height:26px;color:var(--muted)}
.card.featured .card-copy{color:var(--white)}
.card .btn{left:55px;top:410px;width:186px;height:52px}

/* partners */
.partners{left:0;top:2455px;width:1200px;height:258px;background:var(--pale)}
.badge{position:absolute;top:138px;height:44px;background:#c9d6e3;border-radius:8px}

/* news */
.news-card{position:absolute;top:2855px;width:460px;height:490px;background:var(--white);border-top:5px solid var(--orange);box-shadow:0 2px 10px rgba(0,0,0,.1);text-align:center}
.news-card .thumb{height:228px;background:linear-gradient(135deg,#b9c3cc,#6d7f92)}
.news-card h4{margin-top:34px;font-family:"Open Sans",sans-serif;font-weight:400;font-size:22px}
.news-card .date{margin-top:14px;font-family:"Arimo",sans-serif;font-size:15px;font-weight:700;color:var(--orange)}
.news-card p{margin:14px 18px 0;font-family:"Arimo",sans-serif;font-size:14.5px;line-height:24px;color:var(--ink)}
.news-card .btn{left:140px;top:405px;width:182px;height:50px}
.arrow{position:absolute;top:3051px;width:38px;height:38px;border:1px solid var(--orange);border-radius:50%}

/* testimonials */
.quote{position:absolute;top:3622px;width:315px;height:345px;background:var(--white);border-radius:30px;text-align:center}
.quote p{margin:52px 34px 0;font-style:italic;font-size:11.5px;line-height:19px;color:var(--muted)}
.quote .person{position:absolute;left:52px;top:268px;display:flex;gap:14px;text-align:left}
.avatar{width:66px;height:66px;border-radius:50%;border:2px solid var(--orange);background:linear-gradient(135deg,#c9b7a6,#6f5a4c)}
.person b{display:block;font-weight:600;font-size:14px;color:var(--blue);margin-top:10px}
.person small{display:block;font-size:10px;color:var(--muted)}
.dot{position:absolute;top:4028px;width:9px;height:9px;border-radius:50%;background:var(--white)}

/* footer */
.site-footer{left:0;top:4125px;width:1200px;height:407px;background:var(--footer);color:var(--white)}
.site-footer .txt{font-size:12.5px;line-height:22px}
.field{position:absolute;height:28px;background:var(--white);border-radius:3px;font-size:9px;color:#999;padding:6px 10px}
.foot-label{font-family:"Montserrat",sans-serif;font-size:13px;font-weight:500}
.social{width:30px;height:30px;border:2px solid var(--white);border-radius:50%}
.contact-row{display:flex;align-items:flex-start;gap:16px;font-size:13px;line-height:24px}
</style>
</head>
<body>

<header class="site-header abs">
  <div class="brand abs" style="left:113px;top:14px;font-size:26px">
    <span class="brand-mark"></span>Orvane Systems
  </div>
  <nav class="nav">
    <a class="active" href="#">Home</a>
    <a style="left:610px" href="#">Services</a>
    <a style="left:742px" href="#">About Us</a>
    <a style="left:884px" href="#">Helpdesk</a>
    <a style="left:1027px" href="#">Contact</a>
  </nav>
</header>

<section class="hero abs" role="img" aria-label="Teacher presenting in front of a world map display to a class">
  <h1 class="abs">Education, Support and Installation of All<br>Technologies</h1>
  <p class="abs">It is a long established fact that a reader will be distracted by the readable content of a page.</p>
  <a class="btn btn-orange" style="left:517px;top:292px;width:200px;height:58px">GET STARTED
    <svg width="16" height="10" viewBox="0 0 16 10" style="margin-left:10px"><path d="M0 5h14M10 1l4 4-4 4" stroke="#fff" stroke-width="1.6" fill="none"/></svg></a>
</section>
<div class="rule" style="top:560px"></div>

<section class="about">
  <div class="photo-frame abs" style="left:162px;top:645px;width:400px;height:363px">
    <div class="photo" role="img" aria-label="Student working at a computer in a classroom" style="background:linear-gradient(135deg,#8f8472,#3f3a33)"></div>
  </div>
  <h2 class="section-title abs" style="left:660px;top:660px">About Us</h2>
  <div class="body-copy abs" style="left:660px;top:714px;width:430px">
    <p>Orvane Systems, is a registered UK Limited Company</p>
    <p style="margin-top:24px">Our goal is to provide comprehensive ICT support along with excellent customer service to the education sector.</p>
    <p style="margin-top:24px">We offer support in all aspects of ICT in education, from technical faults to assisting teachers and coordinators to meet the requirements of the computing curriculum</p>
  </div>
  <a class="btn btn-orange" style="left:660px;top:947px;width:198px;height:61px">APPLY NOW</a>
</section>

<div class="rule" style="top:1128px"></div>
<section class="band abs" style="top:1136px;height:588px">
  <h2 class="section-title abs" style="left:136px;top:118px;color:#fff;font-size:25px;line-height:40px;width:430px;display:block">Complete Primary and Secondary School Support <span style="display:inline-block;width:24px;height:2px;background:var(--orange);vertical-align:middle;margin-left:10px"></span></h2>
  <p class="body-copy abs" style="left:140px;top:214px;width:430px;font-size:14.5px;line-height:32px">We offer support in all aspects of ICT in education, from technical faults to assisting teachers and coordinators to meet the requirements of the computing curriculum. We offer support in all aspects of ICT in education, from technical faults to meet curriculum.</p>
  <a class="btn btn-white" style="left:147px;top:392px;width:198px;height:60px">APPLY NOW</a>
  <div class="photo-frame abs" style="left:705px;top:89px;width:398px;height:363px">
    <div class="photo" role="img" aria-label="Teachers looking at a laptop together in a library" style="background:linear-gradient(135deg,#a58c6e,#3d5c7a)"></div>
  </div>
</section>
<div class="rule" style="top:1724px"></div>

<section class="services">
  <h2 class="section-title centered abs" style="top:1802px">What we do</h2>
  <div class="card featured" style="left:112px;top:1868px">
    <div class="icon"><span>
      <svg width="60" height="60" viewBox="0 0 60 60" fill="none" stroke="#f26a2a" stroke-width="2.5"><circle cx="30" cy="30" r="9"/><circle cx="30" cy="30" r="18" stroke-dasharray="8 5"/><circle cx="30" cy="30" r="24" stroke-width="1.5"/></svg>
    </span></div>
    <h3>ICT SUPPORT</h3>
    <p class="card-copy">We provide a wide range of ICT support packages, which all include regular onsite visits, telephone, email and helpdesk</p>
    <a class="btn btn-outline" style="border-color:var(--white)">APPLY NOW</a>
  </div>
  <div class="card" style="left:448px;top:1868px">
    <div class="icon"><span>
      <svg width="56" height="56" viewBox="0 0 56 56" fill="none" stroke="#fff" stroke-width="2.5"><rect x="8" y="6" width="40" height="13" rx="2"/><rect x="8" y="22" width="40" height="13" rx="2"/><rect x="8" y="38" width="40" height="13" rx="2"/><circle cx="15" cy="12.5" r="2"/><circle cx="15" cy="28.5" r="2"/><circle cx="15" cy="44.5" r="2"/><path d="M28 12.5h14M28 28.5h14M28 44.5h14"/></svg>
    </span></div>
    <h3>HARDWARE SALES</h3>
    <p class="card-copy">We supply and install hardware from the world's leading manufacturers including: Norvik, Teliam, Arcot, Vexa</p>
    <a class="btn btn-outline">APPLY NOW</a>
  </div>
  <div class="card" style="left:791px;top:1868px">
    <div class="icon"><span>
      <svg width="60" height="56" viewBox="0 0 60 56" fill="none" stroke="#fff" stroke-width="2.5"><path d="M16 38a10 10 0 0 1 0-20 14 14 0 0 1 27-3 11 11 0 0 1 3 22"/><circle cx="33" cy="36" r="8"/><path d="M39 42l8 8"/></svg>
    </span></div>
    <h3 style="top:194px">CLOUD &amp; HOSTING<br>SERVICES</h3>
    <p class="card-copy">We offer an extensive range of cloud and hosting services including websites, domains, blogs, emails and cloud</p>
    <a class="btn btn-outline">APPLY NOW</a>
  </div>
</section>

<section class="partners abs">
  <h2 class="section-title centered abs" style="top:62px">Partners</h2>
  <div class="badge" style="left:172px;width:148px"></div>
  <div class="badge" style="left:380px;width:96px;top:128px;height:60px"></div>
  <div class="badge" style="left:536px;width:146px"></div>
  <div class="badge" style="left:737px;width:112px"></div>
  <div class="badge" style="left:895px;width:134px"></div>
</section>

<section class="news">
  <h2 class="section-title centered abs" style="top:2794px">News</h2>
  <div class="arrow" style="left:40px"><svg width="36" height="36" viewBox="0 0 36 36"><path d="M20 12l-6 6 6 6" stroke="#f26a2a" fill="none" stroke-width="1.5"/></svg></div>
  <article class="news-card" style="left:130px">
    <div class="thumb" role="img" aria-label="Students writing at desks in a classroom"></div>
    <h4>Various versions have evolved over</h4>
    <div class="date">MARCH 14, 2020</div>
    <p>Lorem ipsum dolor sit amet, consectetur adipiscing elit, sed do eiusmod tempor incididunt ut labonvel facilisis.</p>
    <a class="btn btn-outline">VIEW MORE</a>
  </article>
  <article class="news-card" style="left:614px">
    <div class="thumb" role="img" aria-label="Student writing notes in a lecture" style="background:linear-gradient(135deg,#c6cfd8,#5f7890)"></div>
    <h4>Various versions have evolved over</h4>
    <div class="date">MARCH 14, 2020</div>
    <p>Lorem ipsum dolor sit amet, consectetur adipiscing elit, sed do eiusmod tempor incididunt ut labonvel facilisis.</p>
    <a class="btn btn-outline">VIEW MORE</a>
  </article>
  <div class="arrow" style="left:1121px"><svg width="36" height="36" viewBox="0 0 36 36"><path d="M16 12l6 6-6 6" stroke="#f26a2a" fill="none" stroke-width="1.5"/></svg></div>
</section>

<div class="rule" style="top:3422px"></div>
<section class="band abs" style="top:3430px;height:695px">
  <h2 class="section-title centered abs" style="top:92px;color:#fff">Testimonial</h2>
</section>
<svg width="0" height="0" style="position:absolute">
  <defs>
    <g id="stars" fill="#f26a2a"><polygon points="7,0 9,5 14,5 10,8 11.5,13 7,10 2.5,13 4,8 0,5 5,5"/><polygon transform="translate(19 0)" points="7,0 9,5 14,5 10,8 11.5,13 7,10 2.5,13 4,8 0,5 5,5"/><polygon transform="translate(38 0)" points="7,0 9,5 14,5 10,8 11.5,13 7,10 2.5,13 4,8 0,5 5,5"/><polygon transform="translate(57 0)" points="7,0 9,5 14,5 10,8 11.5,13 7,10 2.5,13 4,8 0,5 5,5"/><polygon transform="translate(76 0)" points="7,0 9,5 14,5 10,8 11.5,13 7,10 2.5,13 4,8 0,5 5,5"/></g>
  </defs>
</svg>
<div class="quote" style="left:96px">
  <p>"Orvane Systems are reliable and supportive. Their technical knowledge is fantastic and they make sure our school network runs efficiently. Our school technician, Jamie, is very approachable and friendly. He is always on hand to offer advice and support when needed. He supports the available."</p>
  <div class="person"><div class="avatar" role="img" aria-label="Portrait photo"></div><div><b>Tom Ashdale</b><small>Client, New York City</small>
    <svg width="96" height="14" viewBox="0 0 96 14"><use href="#stars"/></svg></div></div>
</div>
<div class="quote" style="left:442px">
  <p>"Orvane Systems Ltd is extremely competitive price wise and is flexible with their working hours. Regardless of the size of job, the company are always happy to help. Our technician, Dan, has been with us for over 2 years and is very hard working and committed to ensuring we get."</p>
  <div class="person" style="left:42px"><div class="avatar" role="img" aria-label="Portrait photo"></div><div><b>Priya Kenner</b><small>Fennick Labs MD, New York City</small>
    <svg width="96" height="14" viewBox="0 0 96 14"><use href="#stars"/></svg></div></div>
</div>
<div class="quote" style="left:789px">
  <p>"Orvane Systems Ltd is extremely competitive price wise and is flexible with their working hours. Regardless of the size of job, the company are always happy to help. Our technician, Dan, has been with us for over 2 years and is very hard working and committed to ensuring we get the or businesses."</p>
  <div class="person" style="left:48px"><div class="avatar" role="img" aria-label="Portrait photo"></div><div><b>Luis Carrow</b><small>Therapist MSW, New York City</small>
    <svg width="96" height="14" viewBox="0 0 96 14"><use href="#stars"/></svg></div></div>
</div>
<div class="dot" style="left:570px"></div>
<div class="dot" style="left:592px;width:17px;height:17px;top:4024px;background:var(--orange);border:3px solid #fff"></div>
<div class="dot" style="left:621px"></div>

<footer class="site-footer abs">
  <div class="brand abs" style="left:97px;top:48px;font-size:28px">
    <span class="brand-mark"></span>Orvane Systems
  </div>
  <div class="txt abs" style="left:96px;top:112px;width:390px">
    <p>Orvane Systems, is a registered UK Limited Company</p>
    <p style="margin-top:20px">Our goal is to provide comprehensive ICT support along with excellent customer service to the education sector.</p>
    <p style="margin-top:20px">We offer support in all aspects of ICT in education, from technical faults to assisting teachers and coordinators to meet the requirements of the computing curriculum</p>
  </div>

  <div class="foot-label abs" style="left:540px;top:84px">CONTACT US</div>
  <div class="field" style="left:537px;top:120px;width:134px">First Name</div>
  <div class="field" style="left:679px;top:120px;width:134px">Last Name</div>
  <div class="field" style="left:537px;top:156px;width:134px">E-mail</div>
  <div class="field" style="left:679px;top:156px;width:134px">Phone</div>
  <div class="field" style="left:537px;top:192px;width:276px;height:80px">Message</div>
  <a class="btn btn-orange abs" style="left:537px;top:283px;width:134px;height:30px;font-size:10px;font-family:'Open Sans',sans-serif;font-weight:400">Send Message
    <svg width="16" height="11" viewBox="0 0 16 11" style="margin-left:12px"><rect x="0.5" y="0.5" width="15" height="10" fill="#fff"/><path d="M1 1l7 5 7-5" stroke="#f26a2a" fill="none"/></svg></a>

  <div class="foot-label abs" style="left:880px;top:86px">FOLLOW US:</div>
  <div class="abs" style="left:1013px;top:76px;display:flex;gap:7px">
    <span class="social"></span><span class="social"></span><span class="social"></span>
  </div>
  <div class="foot-label abs" style="left:880px;top:126px;font-size:12px">CONTACT INFO</div>
  <div class="contact-row abs" style="left:880px;top:158px">
    <svg width="12" height="18" viewBox="0 0 12 18"><path d="M6 0a6 6 0 0 1 6 6c0 4-6 12-6 12S0 10 0 6a6 6 0 0 1 6-6z" fill="#fff"/><circle cx="6" cy="6" r="2.2" fill="#262a30"/></svg>
    <span>Harlow Court, Millbrook Lane<br>Denfield<br>Westshire<br>DN4 7QR</span>
  </div>
  <div class="contact-row abs" style="left:880px;top:270px">
    <svg width="14" height="14" viewBox="0 0 14 14"><path d="M3 0l3 3-2 2a8 8 0 0 0 5 5l2-2 3 3-2 3C6 14 0 8 0 2z" fill="#fff"/></svg>
    <span>+ 0 155 320 4418</span>
  </div>
  <div class="contact-row abs" style="left:880px;top:304px">
    <svg width="16" height="12" viewBox="0 0 16 12"><rect x="0.5" y="0.5" width="15" height="11" fill="none" stroke="#fff"/><path d="M1 1l7 6 7-6" stroke="#fff" fill="none"/></svg>
    <span>info@orvane-sys.co.uk</span>
  </div>
  <p class="abs" style="left:0;width:1200px;top:376px;text-align:center;font-size:10px">Copyrights © 2020 Allrights Reserved.</p>
</footer>

</body>
</html>
```